Gin Bottle label design

A label for three Gins, 1 Apple flavoured, 1 Bilberry flavoured and one London Dry Gin. All need to incorporate the business logo that i've attached along with the bottle we intend to use. The gin is 40% and will be in a 70cl bottle

```html
<!DOCTYPE html>
<html lang="en">
<head>
<meta charset="utf-8">
<title>London Dry Gin Label</title>
<link href="https://fonts.googleapis.com/css2?family=Arvo:wght@400;700&display=swap" rel="stylesheet">
<style>
  :root {
    --page: #ffffff;
    --navy: #0d1829;
    --navy-deep: #070d18;
    --pattern-light: #24364f;
    --pattern-dark: #0a1220;
    --panel: #e4e5e7;
    --ink: #141414;
    --rule: #f2f2f2;
  }
  html, body {
    margin: 0;
    padding: 0;
    width: 1200px;
    height: 1200px;
    overflow: hidden;
    background: var(--page);
  }
  .canvas {
    position: relative;
    width: 1200px;
    height: 1200px;
  }
  .label {
    position: absolute;
    left: 190px;
    top: 70px;
    width: 820px;
    height: 1060px;
  }
  .label text {
    font-family: "Arvo", serif;
    fill: var(--ink);
  }
  .brand-name {
    font-size: 19px;
    font-weight: 400;
    letter-spacing: 2px;
  }
  .product-name {
    font-size: 76px;
    font-weight: 700;
    letter-spacing: 1px;
  }
  .volume {
    font-size: 28px;
    font-weight: 700;
  }
  .abv {
    font-size: 19px;
    font-weight: 700;
  }
</style>
</head>
<body>
<div class="canvas">
  <svg class="label" viewBox="0 0 820 1060" xmlns="http://www.w3.org/2000/svg">
    <defs>
      <linearGradient id="patternTone" x1="0" y1="0" x2="1" y2="1">
        <stop offset="0" stop-color="var(--pattern-light)"/>
        <stop offset="0.5" stop-color="var(--pattern-dark)"/>
        <stop offset="1" stop-color="var(--pattern-light)"/>
      </linearGradient>
    </defs>

    <!-- outer navy band -->
    <rect class="label-band" x="0" y="0" width="820" height="1060" fill="var(--navy)"/>

    <!-- thin light rule -->
    <rect class="label-rule" x="14" y="40" width="792" height="972" fill="none" stroke="var(--rule)" stroke-width="4"/>

    <!-- botanical pattern area -->
    <rect class="botanical-pattern" x="22" y="48" width="776" height="956" fill="url(#patternTone)"
          role="img" aria-label="Dark navy botanical pattern of leaves, flowers and dotted textures"/>

    <!-- central panel -->
    <rect class="center-panel" x="91" y="184" width="642" height="696" fill="var(--panel)"/>

    <!-- stepped deco frame -->
    <g class="deco-frame" fill="none" stroke="var(--ink)">
      <polygon stroke-width="4" points="130,214 694,214 694,850 130,850"/>
      <polygon stroke-width="2.5" points="175,236 649,236 672,259 672,805 649,828 175,828 152,805 152,259"/>
      <polygon stroke-width="2" points="190,252 634,252 656,274 656,790 634,812 190,812 168,790 168,274"/>
      <line x1="130" y1="290" x2="152" y2="290" stroke-width="2"/>
      <line x1="694" y1="290" x2="672" y2="290" stroke-width="2"/>
      <line x1="130" y1="774" x2="152" y2="774" stroke-width="2"/>
      <line x1="694" y1="774" x2="672" y2="774" stroke-width="2"/>
      <line x1="230" y1="214" x2="230" y2="236" stroke-width="2"/>
      <line x1="594" y1="214" x2="594" y2="236" stroke-width="2"/>
      <line x1="230" y1="850" x2="230" y2="828" stroke-width="2"/>
      <line x1="594" y1="850" x2="594" y2="828" stroke-width="2"/>
    </g>

    <!-- brand -->
    <g class="brand">
      <circle cx="412" cy="352" r="12" fill="var(--ink)"/>
      <text class="brand-name" x="412" y="405" text-anchor="middle">THE OLIVE TABLE</text>
    </g>

    <!-- product -->
    <text class="product-name" x="412" y="600" text-anchor="middle">LONDON</text>
    <text class="product-name" x="412" y="690" text-anchor="middle">DRY GIN</text>

    <!-- details -->
    <text class="volume" x="240" y="789">70cl</text>
    <text class="abv" x="598" y="765" text-anchor="middle">40%</text>
    <text class="abv" x="598" y="791" text-anchor="middle">alc.vol.</text>
  </svg>
</div>
</body>
</html>
```